A website for Veltranor Limited

We need a new and modern website for our company. We are engineering consultants and contractors (EPC) in the oil and gas industry and building services industry.
What we do:
Engineering, procurement, construction
Automation (safety and process)
Non-destructive testing
Training
We have an existing website and the content can be referred from there since we are remaking the website
For more information visit Veltranor Limited Kenya

```html
<!DOCTYPE html>
<html lang="en">
<head>
<meta charset="utf-8">
<title>Veltranor Limited</title>
<link href="https://fonts.googleapis.com/css2?family=Merriweather:ital,wght@0,300;0,400;0,700;0,900;1,300&display=swap" rel="stylesheet">
<style>
:root{
  --orange:#f26a21;
  --ink:#1f1f1f;
  --text:#555555;
  --muted:#8a8a8a;
  --light:#f2f2f2;
  --white:#ffffff;
}
*{margin:0;padding:0;box-sizing:border-box}
html,body{width:1200px;height:4792px;overflow:hidden}
body{position:relative;font-family:'Merriweather',Georgia,serif;color:var(--text);background:var(--white)}
.abs{position:absolute}
.center{text-align:center;left:0;width:1200px}

/* header / hero */
.hero{top:0;left:0;width:1200px;height:730px;background:linear-gradient(160deg,#5c6878 0%,#3b4452 45%,#27303c 100%)}
.hero-shade{top:0;left:0;width:1200px;height:730px;background:linear-gradient(90deg,rgba(20,26,36,.55),rgba(20,26,36,0) 70%)}
.brand{display:flex;align-items:center;gap:10px}
.brand-mark{width:40px;height:40px;border:3px solid var(--orange);flex:none}
.brand-name{font-weight:700;font-size:26px;line-height:1;letter-spacing:.5px}
.brand-sub{font-size:15px;line-height:1;letter-spacing:1px;margin-top:3px;border-bottom:3px solid var(--orange);display:inline-block;padding-bottom:2px}
.header-brand{top:36px;left:80px;color:var(--white)}
.nav{top:46px;left:388px;display:flex;gap:36px;font-size:14px;color:var(--white)}
.phone{top:40px;left:965px;display:flex;align-items:center;gap:12px;color:var(--white);font-size:14px}
.phone-dot{width:30px;height:30px;border-radius:50%;background:var(--orange);display:flex;align-items:center;justify-content:center}
.hero-title{top:290px;left:149px;color:var(--white);font-weight:700;font-size:40px;letter-spacing:.5px;line-height:1.2}
.hero-sub{top:345px;left:149px;color:var(--white);font-weight:700;font-size:26px;line-height:1.12}
.btn{background:var(--orange);color:var(--white);font-weight:700;font-size:14px;letter-spacing:.5px;display:flex;align-items:center;justify-content:center;text-transform:uppercase}
.hero-btn{top:437px;left:149px;width:162px;height:44px}

.heading{font-weight:900;font-size:38px;line-height:1.2;color:var(--ink);letter-spacing:.5px}
.heading::after{content:"";display:block;width:96px;height:5px;background:var(--orange);margin:10px auto 0}
.heading-light{color:var(--white)}

/* who */
.who-text{top:875px;font-size:17px;line-height:25px;font-weight:300}
.who-bold{top:970px;font-size:21px;line-height:27px;font-weight:700;color:var(--ink)}
.industry{top:1062px;width:430px;height:303px}
.industry-img{width:100%;height:100%}
.industry-label{position:absolute;left:26px;right:26px;top:220px;height:57px;background:var(--orange);color:var(--white);font-size:25px;display:flex;align-items:center;justify-content:center}

/* what we do */
.what{top:1503px;left:0;width:1200px;height:753px;background:var(--light)}
.service{width:460px;height:122px;display:flex;gap:22px}
.service-icon{width:139px;height:122px;flex:none;display:flex;align-items:center;justify-content:center}
.service-icon.solid{background:var(--orange)}
.service-icon.outline{border:3px solid var(--orange);background:var(--white)}
.service-icon span{width:62px;height:62px;border-radius:8px}
.solid span{background:rgba(255,255,255,.35)}
.outline span{background:#e4e4e4}
.service h3{font-size:19px;font-weight:700;color:var(--ink);margin:16px 0 6px}
.service p{font-size:12.5px;line-height:18px;font-weight:300;color:#444;width:260px}

/* works */
.works{top:2256px;left:0;width:1200px;height:819px;background:linear-gradient(120deg,#555 0%,#3f3f3f 55%,#4d4d4d 100%)}
.view-btn{top:2950px;left:515px;width:162px;height:45px;box-shadow:6px 6px 0 rgba(242,106,33,.45)}

/* testimonials */
.testi-quote{top:3280px;left:210px;width:780px;text-align:center;font-style:italic;font-weight:300;font-size:19px;line-height:29px;color:#555}
.avatar{top:3395px;left:480px;width:102px;height:102px;border-radius:50%;background:linear-gradient(135deg,#c9a24a,#6f6a3e)}
.person{top:3425px;left:595px}
.person b{font-size:17px;font-weight:400;color:var(--ink);display:block}
.person small{font-size:11px;color:var(--muted)}

.partners{top:3700px;left:120px;width:960px;display:flex;justify-content:space-between;align-items:center}
.partner{display:flex;align-items:center;gap:10px;font-weight:700;font-size:20px;color:#3a3a3a}
.partner i{width:34px;height:34px;border-radius:50%;background:#3a3a3a;display:block}

/* quote */
.quote{top:3884px;left:0;width:1200px;height:446px;background:linear-gradient(90deg,#f06a24,#f4793a 60%,#ef6a22)}
.quote-title{top:3960px;font-weight:700;font-size:26px;line-height:1.2;color:#ffe2cf}
.quote-title::after{content:"";display:block;width:56px;height:3px;background:#ffe2cf;margin:6px auto 0}
.field{background:var(--white);font-size:12px;color:#888;padding:10px 12px}
.submit{top:4207px;left:541px;width:120px;height:46px;background:#1f1f1f;color:var(--white);font-weight:700;font-size:14px;display:flex;align-items:center;justify-content:center;letter-spacing:.5px}

/* footer */
.footer-brand{top:4448px;left:152px;color:var(--ink)}
.foot-about{top:4520px;left:152px;width:280px;font-size:13px;line-height:20px;font-weight:300}
.foot-col h4{font-size:14px;font-weight:700;color:var(--ink);letter-spacing:.5px}
.foot-col h4::after{content:"";display:block;width:68px;height:2px;background:var(--orange);margin-top:14px}
.foot-col ul{list-style:none;margin-top:18px;font-size:13px;line-height:24px;font-weight:300;padding-left:7px}
.foot-col p{margin-top:18px;font-size:13px;line-height:20px;font-weight:300;width:200px}
.socials{display:flex;gap:10px;margin-top:16px}
.socials i{width:22px;height:22px;border-radius:50%;background:var(--orange);display:block}
.copy{top:4700px;font-size:14px;color:#333;font-weight:300}
</style>
</head>
<body>

<!-- Hero -->
<section class="abs hero" role="img" aria-label="Engineer in hard hat and safety vest holding plans over a construction site with cranes"></section>
<div class="abs hero-shade"></div>
<div class="abs brand header-brand">
  <div class="brand-mark"></div>
  <div><div class="brand-name">VELTRANOR</div><div class="brand-sub">LIMITED</div></div>
</div>
<nav class="abs nav"><span>Home</span><span>About Us</span><span>What we do</span><span>Team</span><span>Projects</span><span>Contact</span></nav>
<div class="abs phone">
  <span class="phone-dot"><svg width="14" height="14" viewBox="0 0 24 24"><path fill="#fff" d="M6.6 10.8a15 15 0 0 0 6.6 6.6l2.2-2.2c.3-.3.7-.4 1-.2 1.1.4 2.3.6 3.6.6.6 0 1 .4 1 1V20c0 .6-.4 1-1 1A17 17 0 0 1 3 4c0-.6.4-1 1-1h3.5c.6 0 1 .4 1 1 0 1.3.2 2.5.6 3.6.1.3 0 .7-.2 1z"/></svg></span>
  (555) 014 2290
</div>
<h1 class="abs hero-title">VELTRANOR LIMITED</h1>
<p class="abs hero-sub">&nbsp;We are engineering consultants<br>and contractors</p>
<div class="abs btn hero-btn">Learn more</div>
<svg class="abs" style="top:640px;left:0" width="1200" height="92" viewBox="0 0 1200 92">
  <polygon points="0,20 560,44 0,90" fill="#f26a21"/>
  <polygon points="0,90 1200,66 1200,92 0,92" fill="#ffffff"/>
</svg>

<!-- Who we are -->
<h2 class="abs center heading" style="top:788px">WHO WE ARE</h2>
<p class="abs center who-text">Lorem ipsum dolor sit amet, consectetur adipiscing elit, sed do eiusmod tempor<br>incididunt ut labore et dolore magna aliqua. Quis ipsum suspendisse ultrices gravida.<br>Risus commodo viverra maecenas accumsan lacus vel facilisis.</p>
<p class="abs center who-bold">We are engineering consultants and contractors (EPC) in the<br>oil and gas industry and building services industry.</p>
<div class="abs industry" style="left:149px">
  <div class="industry-img" role="img" aria-label="Oil refinery towers at sunset" style="background:linear-gradient(180deg,#c9b6a6 0%,#e0a86a 45%,#3b3a40 100%)"></div>
  <div class="industry-label">Oil and Gas Industry</div>
</div>
<div class="abs industry" style="left:599px">
  <div class="industry-img" role="img" aria-label="Site engineers reviewing plans on a building site" style="background:linear-gradient(180deg,#d9c7ae 0%,#b89c7c 50%,#6d6558 100%)"></div>
  <div class="industry-label">Building services industry</div>
</div>

<!-- What we do -->
<section class="abs what"></section>
<h2 class="abs center heading" style="top:1592px">WHAT WE DO</h2>
<div class="abs service" style="top:1713px;left:151px"><div class="service-icon solid" role="img" aria-label="Engineering icon"><span></span></div><div><h3>Engineering</h3><p>Lorem ipsum dolor sit amet, consectetur adipiscing elit, sed do eiusmod tempor incididunt ut labore et dolore mlodagna aliquis ipsum suspendisse.</p></div></div>
<div class="abs service" style="top:1713px;left:636px"><div class="service-icon outline" role="img" aria-label="Procurement icon"><span></span></div><div><h3>Procurement</h3><p>Lorem ipsum dolor sit amet, consectetur adipiscing elit, sed do eiusmod tempor incididunt ut labore et dolore mlodagna aliquis ipsum suspendisse.</p></div></div>
<div class="abs service" style="top:1869px;left:151px"><div class="service-icon outline" role="img" aria-label="Construction icon"><span></span></div><div><h3>Construction</h3><p>Lorem ipsum dolor sit amet, consectetur adipiscing elit, sed do eiusmod tempor incididunt ut labore et dolore mlodagna aliquis ipsum suspendisse.</p></div></div>
<div class="abs service" style="top:1869px;left:636px"><div class="service-icon solid" role="img" aria-label="Automation icon"><span></span></div><div><h3>Automation</h3><p>Lorem ipsum dolor sit amet, consectetur adipiscing elit, sed do eiusmod tempor incididunt ut labore et dolore mlodagna aliquis ipsum suspendisse.</p></div></div>
<div class="abs service" style="top:2025px;left:151px"><div class="service-icon solid" role="img" aria-label="Non-destructive testing icon"><span></span></div><div><h3>Non-destructive testing</h3><p>Lorem ipsum dolor sit amet, consectetur adipiscing elit, sed do eiusmod tempor incididunt ut labore et dolore mlodagna aliquis ipsum suspendisse.</p></div></div>
<div class="abs service" style="top:2025px;left:636px"><div class="service-icon outline" role="img" aria-label="Training icon"><span></span></div><div><h3>Training</h3><p>Lorem ipsum dolor sit amet, consectetur adipiscing elit, sed do eiusmod tempor incididunt ut labore et dolore mlodagna aliquis ipsum suspendisse.</p></div></div>

<!-- Our works -->
<section class="abs works" role="img" aria-label="Muted background of engineers discussing drawings"></section>
<h2 class="abs center heading heading-light" style="top:2336px">OUR WORKS</h2>
<div class="abs" style="top:2446px;left:154px;width:592px;height:223px;background:linear-gradient(90deg,#b8521c,#e0732d 50%,#9a4416)" role="img" aria-label="Refinery and engineer in orange highlight"></div>
<svg class="abs" style="top:2532px;left:420px" width="56" height="56" viewBox="0 0 56 56"><circle cx="22" cy="22" r="17" fill="none" stroke="#fff" stroke-width="3"/><line x1="34" y1="34" x2="50" y2="50" stroke="#fff" stroke-width="4"/><line x1="14" y1="22" x2="30" y2="22" stroke="#fff" stroke-width="3"/><line x1="22" y1="14" x2="22" y2="30" stroke="#fff" stroke-width="3"/></svg>
<div class="abs" style="top:2446px;left:763px;width:288px;height:223px;background:linear-gradient(180deg,#e9e4dc,#a99c8a)" role="img" aria-label="Two engineers reviewing plans inside a building"></div>
<div class="abs" style="top:2682px;left:154px;width:291px;height:223px;background:linear-gradient(180deg,#eeeeee,#8f9a8c)" role="img" aria-label="Hands working on technical drawings"></div>
<div class="abs" style="top:2682px;left:458px;width:290px;height:223px;background:linear-gradient(180deg,#c9cfd8,#b59a78)" role="img" aria-label="Engineers on a construction site with cranes"></div>
<div class="abs" style="top:2682px;left:763px;width:288px;height:223px;background:linear-gradient(135deg,#6f8aa8,#c76b3a)" role="img" aria-label="Engineer with laptop at an industrial plant"></div>
<div class="abs btn view-btn">View all</div>

<!-- Testimonials -->
<svg class="abs" style="top:3075px;left:0" width="1200" height="555" viewBox="0 0 1200 555"><polygon points="0,0 1200,0 1200,552 0,459" fill="#f0eff0"/></svg>
<h2 class="abs center heading" style="top:3158px">TESTIMONIALS</h2>
<p class="abs testi-quote">Lorem ipsum dolor sit amet, consectetur adipiscing elit, sed do eiusmod tempor incididunt ut labore et dolore magna aliqua. Quis ipsum suspendisse ultrices gravida. Risus commodo viverra maecenas accumsan lacus vel facilisis.</p>
<div class="abs avatar" role="img" aria-label="Portrait of client in hard hat"></div>
<div class="abs person"><b>MAREK OLUSANYA</b><small>Lorem Ipsum</small></div>

<div class="abs partners">
  <div class="partner"><i></i>BRENHOLT</div>
  <div class="partner"><i></i>QUARVEX</div>
  <div class="partner"><i></i>TAMSEL</div>
  <div class="partner"><i></i>ORINDALE</div>
  <div class="partner"><i></i>KESTROVA</div>
</div>

<!-- Quote -->
<section class="abs quote" role="img" aria-label="Orange tinted construction site with worker"></section>
<h2 class="abs center quote-title">GET A QUOTE</h2>
<div class="abs field" style="top:4027px;left:333px;width:259px;height:38px">Name :</div>
<div class="abs field" style="top:4027px;left:599px;width:286px;height:38px">Phone :</div>
<div class="abs field" style="top:4079px;left:333px;width:259px;height:38px">Email :</div>
<div class="abs field" style="top:4079px;left:599px;width:286px;height:38px">Subject:</div>
<div class="abs field" style="top:4127px;left:333px;width:552px;height:110px">Message :</div>
<div class="abs submit">SUBMIT</div>

<!-- Footer -->
<footer>
  <div class="abs brand footer-brand">
    <div class="brand-mark"></div>
    <div><div class="brand-name">VELTRANOR</div><div class="brand-sub">LIMITED</div></div>
  </div>
  <p class="abs foot-about">Lorem ipsum dolor sit amet, consectetur adipiscing elit, sed do eiusmod tempor incididunt ut labore et dolore magna aliqua. Quis ipsum suspendisse ultrices</p>
  <div class="abs foot-col" style="top:4448px;left:493px"><h4>QUICK LINKS</h4><ul><li>Home</li><li>About Us</li><li>Services</li><li>News</li><li>Contact</li></ul></div>
  <div class="abs foot-col" style="top:4448px;left:681px"><h4>SUPPORT</h4><ul><li>Support</li><li>Help</li><li>Privacy Policy</li><li>Terms and Conditions</li></ul></div>
  <div class="abs foot-col" style="top:4448px;left:876px"><h4>CONNECT ME</h4><p>Lorem ipsum dolor sit amet ons ectetur adipisciliuis</p><div class="socials"><i aria-label="Social link"></i><i aria-label="Social link"></i><i aria-label="Social link"></i></div></div>
  <p class="abs center copy">Copyrights © 2023 Veltranor Limited. All rights Reserved</p>
</footer>

</body>
</html>
```